Kambo Flyer

to create a Flyer with information about Kambo Ceremonies. The flyer that is up loaded is an example

Requirements
Must have
• Benefits of Kambo
• Kambo is traditionally known to be anti-inflammatory, to relieve joint pain, to heal eyesight, and to ease pain. Kambo peptides, and their effects, are reported to cover a wide range of potential medical uses: treatment of brain diseases such as Alzheimer’s and Parkinson’s, depression, migraines, blood circulation problems, vascular insufficiency, organ diseases, skin and eyes issues, cancer, fertility problems in women, AIDS, candida, hepatitis, herpes, and more
• What is Kambo
• The scientific name for this frog is Phyllomedusa bicolor or “Two-Colored Leaf Guardian.” It is also known as the “Giant Green Monkey Tree Frog.”
• Kambo is legal in the United States, as well as all other countries, and is not a hallucinogenic. It is, however, a deep cleansing therapy – – physically, emotionally and mentally. It is one of the world’s most effective and natural antibiotics and immune system boosters. It detoxifies the liver and intestines, improves mental functioning, and has the potential to dissolve emotional blocks. It also helps to reset our cellular memory.
• Please note that fasting 12 hours prior to the ceremony is required
• Private (in Home} Semi-Private and Group Ceremonies Available
• For More information see our website
• www.MeadowLightHalls.org
• 555-214-0873
• Traditional Shamanic Kambo Ceremonies in Florida

```html
<!DOCTYPE html>
<html lang="en">
<head>
<meta charset="utf-8">
<title>Traditional Shamanic Kambo Ceremonies – Flyer</title>
<link rel="stylesheet" href="https://fonts.googleapis.com/css2?family=Cinzel:wght@400;700&family=Cormorant+Garamond:wght@700&family=Lora:ital,wght@1,500&family=Lato:wght@400;700&family=Questrial&display=swap">
<style>
  :root {
    --leaf-dark: #1e6b1e;
    --leaf: #4f9a2a;
    --leaf-light: #8cc63f;
    --lime: #a9d86b;
    --panel: #93cc5c;
    --badge: #1f2420;
    --bar: #343434;
    --ink: #2a2a2a;
    --paper: #ffffff;
    --stage: #e9ebe8;
    --gold: #e3c88b;
  }
  * { box-sizing: border-box; margin: 0; padding: 0; }
  html, body { width: 1200px; height: 1200px; overflow: hidden; background: var(--stage); }
  .flyer {
    position: absolute; left: 141px; top: 6px;
    width: 918px; height: 1188px;
    background: var(--paper); overflow: hidden;
    font-family: "Lato", sans-serif; color: var(--ink);
  }
  .hero { position: absolute; left: 0; top: 0; width: 918px; height: 480px; }
  .hero-scene {
    position: absolute; inset: 0 0 40px 0;
    background: linear-gradient(160deg, #4d7a2c 0%, #7fae44 35%, #3e6a25 60%, #9bbd6a 80%, #c9b58d 100%);
  }
  .hero-wave { position: absolute; left: 0; top: 370px; width: 918px; height: 110px; }

  .frog-photo {
    position: absolute; left: 31px; top: 330px; width: 440px; height: 150px; z-index: 1;
    border-radius: 55% 45% 30% 30% / 70% 70% 30% 30%;
    background: radial-gradient(ellipse at 40% 40%, #a6e04a, #6fae22 70%, #5b8a2a);
  }

  .badge {
    position: absolute; left: 287px; top: 38px; width: 306px; height: 306px; z-index: 2;
    border-radius: 50%; background: var(--badge);
    box-shadow: 0 0 0 8px rgba(255,255,255,.18);
    text-align: center; color: #fff;
  }
  .badge-traditional { font-family: "Cormorant Garamond", serif; font-weight: 700; font-size: 28px; line-height: 30px; color: var(--gold); margin-top: 27px; }
  .badge-shamanic { font-family: "Lora", serif; font-style: italic; font-size: 40px; line-height: 44px; margin-top: 2px; }
  .badge-kambo { font-family: "Cinzel", serif; font-weight: 700; font-size: 64px; line-height: 56px; color: var(--leaf-light); letter-spacing: 1px; }
  .badge-ceremonies { font-family: "Cinzel", serif; font-size: 30px; color: var(--leaf-light); line-height: 36px; }
  .badge-place { font-weight: 700; font-size: 19px; line-height: 24px; margin-top: 8px; }
  .badge-types { font-size: 14.5px; color: var(--lime); margin-top: 2px; line-height: 19px; }
  .badge-limited { font-size: 15.5px; line-height: 20px; margin-top: 6px; }

  .side-panel {
    position: absolute; left: 632px; top: 440px; width: 235px; height: 653px;
    background: var(--panel); border-radius: 0 0 6px 6px;
  }
  .side-photo {
    position: absolute; left: 37px; width: 166px; height: 166px; border-radius: 50%;
    border: 5px solid #c6e7a2;
  }
  .side-photo.ritual { top: 57px; background: radial-gradient(circle at 60% 40%, #b24a2a, #5a2416); }
  .side-photo.hands { top: 252px; background: radial-gradient(circle at 40% 55%, #e0a56a, #6c7c8c); }
  .side-photo.guide { top: 449px; background: radial-gradient(circle at 50% 55%, #d8b07e, #f4e7ec); }

  h2.section-title { position: absolute; left: 40px; font-family: "Lato", sans-serif; font-weight: 700; font-size: 26px; color: var(--leaf-dark); }
  .benefits-title { top: 496px; }
  .what-title { top: 655px; left: 42px; }
  .benefits-text {
    position: absolute; left: 42px; top: 533px; width: 569px;
    font-size: 14.4px; line-height: 18px; text-align: justify;
  }
  .species-text { position: absolute; left: 42px; top: 692px; width: 580px; font-size: 17.4px; line-height: 22px; }
  .species-text strong { color: var(--leaf-dark); font-weight: 700; }
  .legal-text {
    position: absolute; left: 150px; top: 749px; width: 462px;
    font-size: 13px; line-height: 17.5px; text-align: justify; text-align-last: left;
  }

  .guide-photo {
    position: absolute; left: 0; top: 745px; width: 211px; height: 443px;
    background: linear-gradient(180deg, #eef0f6 0%, #f5f5f5 40%, #e6e6e6 100%);
    border-radius: 80px 80px 0 0;
  }

  .offer-title {
    position: absolute; left: 199px; top: 868px;
    font-family: "Questrial", sans-serif; font-size: 21px; line-height: 26px; font-weight: 700;
  }

  .schedule {
    position: absolute; left: 256px; top: 945px; width: 339px; height: 155px;
    border: 2px solid var(--lime); border-radius: 8px;
    background: linear-gradient(180deg, #ffffff, #ececec);
    text-align: center;
  }
  .schedule-icon {
    position: absolute; left: -38px; top: 0; width: 74px; height: 74px; border-radius: 50%;
    background: #fff; border: 3px solid var(--lime);
    display: flex; align-items: center; justify-content: center;
  }
  .schedule-dates { font-size: 26px; margin-top: 9px; padding-left: 40px; color: var(--ink); }
  .schedule-times { font-size: 27px; font-weight: 700; color: var(--leaf-dark); line-height: 33px; }
  .schedule-note { font-family: "Questrial", sans-serif; font-size: 14.5px; line-height: 18px; margin-top: 8px; }

  .more-info { position: absolute; left: 607px; top: 1110px; font-weight: 700; font-size: 14.5px; }

  .contact-bar {
    position: absolute; left: 193px; top: 1133px; width: 725px; height: 55px;
    background: var(--bar); color: #fff; display: flex; align-items: center;
  }
  .contact-phone { position: absolute; left: 97px; display: flex; align-items: center; gap: 14px; font-size: 26px; font-weight: 700; }
  .contact-web { position: absolute; left: 410px; display: flex; align-items: center; gap: 14px; font-size: 16px; }
</style>
</head>
<body>
<main class="flyer">

  <section class="hero">
    <div class="hero-scene" role="img" aria-label="Rainforest with ferns, trees and a wooden boardwalk path"></div>
    <svg class="hero-wave" viewBox="0 0 918 110" preserveAspectRatio="none" aria-hidden="true">
      <path d="M0 48 C150 0 300 0 460 40 C640 85 800 80 918 20 L918 110 L0 110 Z" fill="var(--leaf-light)"/>
      <path d="M0 62 C150 14 300 14 460 54 C640 99 800 94 918 34 L918 110 L0 110 Z" fill="var(--leaf)"/>
      <path d="M0 72 C150 26 300 26 460 66 C640 110 800 104 918 46 L918 110 L0 110 Z" fill="var(--paper)"/>
    </svg>

    <div class="frog-photo" role="img" aria-label="Giant green monkey tree frog sitting"></div>

    <div class="badge">
      <p class="badge-traditional">Traditional</p>
      <p class="badge-shamanic">Shamanic</p>
      <p class="badge-kambo">KAMBO</p>
      <p class="badge-ceremonies">CEREMONIES</p>
      <p class="badge-place">IN FLORIDA!</p>
      <p class="badge-types">Private &nbsp;•&nbsp; Semi-Private &nbsp;•&nbsp; Group<br>Ceremonies available</p>
      <p class="badge-limited">LIMTED SPOTA</p>
    </div>
  </section>

  <aside class="side-panel">
    <div class="side-photo ritual" role="img" aria-label="Artwork of a tree frog during a kambo ritual"></div>
    <div class="side-photo hands" role="img" aria-label="Practitioner applying kambo to a shoulder"></div>
    <div class="side-photo guide" role="img" aria-label="Portrait of a ceremony facilitator"></div>
  </aside>

  <h2 class="section-title benefits-title">Benefits of Kambo</h2>
  <p class="benefits-text">Kambo is traditionally known to be anti-inflammatory, to relieve joint pain, to heal eyesight, and to ease pain. Kambo peptides, and their effects, are reported to cover a wide range of potential medical uses: treatment of brain diseases such as Alzheimer’s and Parkinson’s, depression, migraines, blood circulation problems, vascular insufficiency, organ diseases, skin and eyes issues, cancer, fertility problems in women, AIDS, candida, hepatitis, herpes, and more</p>

  <h2 class="section-title what-title">What is Kambo</h2>
  <p class="species-text">The scientific name for this frog is Phyllomedusa bicolor or “<strong>Two-Colored Leaf Guardian</strong>.” It is also known as the “<strong>Giant Green Monkey Tree Frog</strong>.”</p>

  <div class="guide-photo" role="img" aria-label="Shaman in white shirt wearing a beaded necklace and headband"></div>

  <p class="legal-text">Kambo is legal in the United States, as well as all other countries, and is not a hallucinogenic. It is, however, a deep cleansing therapy – – physically, emotionally and mentally. It is one of the world’s most effective and natural antibiotics and immune system boosters. It detoxifies the liver and intestines, improves mental functioning, and has the potential to dissolve emotional blocks. It also helps to reset our cellular memory.</p>

  <h3 class="offer-title">Private (in Home) Semi-Private &amp; Group<br>&nbsp;Ceremonies Available</h3>

  <div class="schedule">
    <div class="schedule-icon">
      <svg width="42" height="42" viewBox="0 0 42 42" aria-hidden="true" fill="none" stroke="#8a8a8a" stroke-width="2.5">
        <rect x="3" y="7" width="30" height="28" rx="3"/>
        <line x1="3" y1="14" x2="33" y2="14"/>
        <line x1="11" y1="3" x2="11" y2="10"/><line x1="25" y1="3" x2="25" y2="10"/>
        <path d="M9 20h4M17 20h4M9 26h4M17 26h4"/>
        <circle cx="32" cy="32" r="8" fill="#fff"/>
        <path d="M32 27v5l3 2"/>
      </svg>
    </div>
    <p class="schedule-dates">DEC 8th - 10th-12th</p>
    <p class="schedule-times">9.00am, 1:00 pm<br>or 7:00 pm</p>
    <p class="schedule-note">Please note that fasting <strong>12 hours</strong> prior<br>to the ceremony is required</p>
  </div>

  <p class="more-info">For More information see our website</p>

  <footer class="contact-bar">
    <div class="contact-phone">
      <svg width="26" height="26" viewBox="0 0 24 24" aria-hidden="true" fill="none" stroke="#fff" stroke-width="1.8">
        <path d="M5 3h4l2 5-2.5 1.5a11 11 0 0 0 6 6L16 13l5 2v4a2 2 0 0 1-2 2A17 17 0 0 1 3 5a2 2 0 0 1 2-2z"/>
        <path d="M15 3a6 6 0 0 1 6 6M15 7a2 2 0 0 1 2 2"/>
      </svg>
      <span>555-214-0873</span>
    </div>
    <div class="contact-web">
      <svg width="14" height="14" viewBox="0 0 24 24" aria-hidden="true" fill="none" stroke="#fff" stroke-width="2">
        <circle cx="12" cy="12" r="10"/><path d="M2 12h20M12 2c3 3 3 17 0 20M12 2c-3 3-3 17 0 20"/>
      </svg>
      <span>www.MeadowLightHalls.org</span>
    </div>
  </footer>

</main>
</body>
</html>
```